Holistic Health Coach needs simple web site design for a new practice

I need a web (re)design for my entire site, Birchwell Sprout Lady. I have a beautiful new blue and green logo that I'd like the site fonts and color scheme to be built around. I'll attach my new logo so you'll know the colors/design feel I'm after.

I want easy navigation for my mostly text based site, widgets for my social media pages and a clean, fun, light feel for the site.

Target Market(s)

People looking to take charge of their own health, and who may need my coaching services to obtain optimal wellness.

Industry/Entity Type

Health

Coding

Coded - Design and coding required

Number of Pages Required

5+ page

Font styles to use
Script

Colors
33b8a4
33a6d7
ffffff

Requirements
Must have
• Must incorporate my logo design, as well as same/similar fonts and color scheme.
• I'd like it to stay as close to the current design as possible.
Nice to have
• Would love to incorporate a hover over menu (for example, when a user hovers over "About", they will see the submenu in a floating design.
Should not have
• No dark colors or masculine feel

```html
<!DOCTYPE html>
<html lang="en">
<head>
<meta charset="utf-8">
<title>Birchwell Sprout Lady</title>
<link rel="stylesheet" href="https://fonts.googleapis.com/css2?family=Dancing+Script:wght@600&family=Open+Sans:wght@400;600;700&display=swap">
<style>
:root{
  --teal:#33b8a4;
  --blue:#33a6d7;
  --white:#ffffff;
  --page:#eef5fb;
  --ink:#555b60;
  --muted:#9aa3aa;
  --line:#e3e9ee;
  --apple:#c8262c;
  --orange:#e8692d;
  --skin:#b89a86;
  --pink:#f6b3b8;
}
*{box-sizing:border-box;margin:0;padding:0}
html,body{width:676px;height:1200px;overflow:hidden}
body{background:var(--page);font-family:"Open Sans",Arial,sans-serif;color:var(--ink);position:relative}
.site-header{height:34px;background:var(--white);display:flex;align-items:center;justify-content:space-between;padding:0 56px 0 108px;box-shadow:0 1px 2px rgba(0,0,0,.05)}
.brand{font-family:"Dancing Script",cursive;font-weight:600;font-size:14px;color:var(--teal);display:flex;align-items:center;gap:4px}
.brand-dot{width:5px;height:5px;border-radius:50%;background:var(--blue)}
.main-nav{display:flex;gap:13px;font-size:5.5px;font-weight:600;text-transform:uppercase;letter-spacing:.2px}
.main-nav a{color:var(--ink);text-decoration:none}
.main-nav a.active{color:var(--blue)}
.submenu{position:absolute;top:27px;left:357px;width:76px;background:var(--white);box-shadow:0 2px 4px rgba(0,0,0,.12);font-size:5px}
.submenu a{display:block;padding:3px 7px;color:var(--ink);text-decoration:none}
.submenu a.current{background:var(--teal);color:var(--white)}
.content{position:absolute;top:47px;left:88px;width:353px}
.sidebar{position:absolute;top:47px;left:426px;width:220px}
.post{background:var(--white);padding:12px 22px 14px;margin-bottom:38px;box-shadow:0 1px 2px rgba(0,0,0,.04)}
.post-title{font-family:"Dancing Script",cursive;font-weight:600;font-size:18px;line-height:1.15;color:var(--blue);margin-bottom:14px}
.post-meta{font-size:5.8px;color:var(--muted);margin-bottom:8px}
.post p{font-size:6.2px;line-height:1.65;margin-bottom:8px}
.post a{color:var(--blue);text-decoration:none}
.figure{display:block;margin:8px auto 12px}
.figure-apple{width:40px;height:44px;background:radial-gradient(circle at 45% 55%,#d9373c,var(--apple));border-radius:46% 46% 50% 50%}
.figure-portrait{width:44px;height:46px;background:linear-gradient(135deg,#d8c4b5,var(--skin) 60%,#6d5a4d)}
.figure-badge{width:58px;height:58px;border-radius:50%;background:var(--orange)}
.figure-flyer{width:120px;height:60px;background:linear-gradient(180deg,#f9c8cc,var(--pink));margin-bottom:0}
.links p{margin-bottom:4px}
.read-more{display:flex;justify-content:flex-end;margin-top:6px}
.btn{background:var(--blue);color:var(--white);font-size:5px;font-weight:700;padding:5px 8px;border-radius:2px;text-transform:uppercase}
.widget{background:var(--white);padding:10px 12px 8px;margin-bottom:12px}
.search{display:flex;gap:4px}
.search-field{flex:1;height:12px;border:1px solid var(--line);font-size:5px;color:var(--muted);padding:2px 4px}
.search-btn{width:12px;height:12px;background:var(--blue);display:flex;align-items:center;justify-content:center}
.widget-title{font-size:5.8px;font-weight:600;font-style:italic;color:var(--teal);text-transform:uppercase;margin:2px 0 6px}
.widget ul{list-style:none}
.widget li{font-size:5.6px;line-height:1.5;padding:4px 0;border-bottom:1px solid var(--line)}
.widget li:last-child{border-bottom:none}
.widget li a{color:var(--ink);text-decoration:none}
.widget li .by{color:var(--teal)}
.widget li .mark{display:inline-block;width:4px;height:4px;border:1px solid var(--muted);margin-right:3px}
.to-top{position:absolute;right:24px;bottom:14px;width:12px;height:12px;background:#c7cfd6;display:flex;align-items:center;justify-content:center}
</style>
</head>
<body>
<header class="site-header">
  <div class="brand"><span>Birchwell Sprout Lady</span><span class="brand-dot"></span></div>
  <nav class="main-nav">
    <a href="#">Home</a>
    <a href="#" class="active">About Me ▾</a>
    <a href="#">Essential Oils</a>
    <a href="#">Three-Week Sugar Reset Coaching Services</a>
  </nav>
</header>
<div class="submenu">
  <a href="#" class="current">Sub-link 1</a>
  <a href="#">Sub-link 2</a>
</div>

<main class="content">
  <article class="post">
    <h1 class="post-title">Lifestyles of the Tired and Wired – Module 4 of Root Reset: Adrenal Fatigue</h1>
    <div class="post-meta">April 19, 2015 &nbsp; 🗨 Leave a comment</div>
    <p>As the title suggests, Module 4 of Root Reset: Adrenal Fatigue is all about lifestyle factors. Specifically, how you can make changes to your lifestyle in the areas of stress, sleep, social connection, and exercise and recovery.</p>
    <div class="figure figure-apple" role="img" aria-label="Illustration of a red apple with a cross emblem"></div>
    <p>I've been dreading this module because when I got my diagnosis, I was told that once I got my stress under control, my symptoms would go away. Which is partially true, but I had to make dietary changes, and undergo treatment for it before I really started seeing improvement. And I wasn't sure there wasn't anything I could learn that I didn't already know in these areas.</p>
    <p>The first lesson in Module 4 covered stress management. There was a video discussing the effects of stress on the body, why stress management is so important, and several ideas that you can implement right away to help minimize the damage stress inflicts on the body. I think my favorite tools were the Stress Management Log and the variety of stress management tools they recommended – most of which were absolutely FREE. After just a few days of implementing the suggestions I selected, I am starting to see a difference in my mood and energy levels 🙂</p>
    <div class="figure figure-portrait" role="img" aria-label="Photo of the author resting with a sleep mask"></div>
    <p>Next is sleep. No, I don't mean its time for a nap, but if you need one, by all means, take one and read this later. As in the previous lesson, I really thought I had this one nailed. Until I read the section about electronics and screen time. I 'knew' that you're not supposed to expose yourself to blue light after dark, or if you do, you should wear those funky looking orange glasses, because of its effect on your sleep, but I wasn't doing it. You see, blogging isn't my only job, and I have to work around my 9 to 5 job to find time to blog. Oftentimes, that means writing before the sun comes up or after it goes down. I do have <a href="#">Dimmer</a> on my laptop, which helps A LOT, but then I'm often checking my phone, which until recently didn't have any sort of dimmer during the evening and early morning. I recently installed <a href="#">Dusklight</a> on my smartphone as well. However, I was still checking my phone while in bed trying to get to sleep. If you're doing that, stop it. Really, I know it seems like an easy thing to do, but don't. It just really messes with your sleep, which is what you're trying to avoid, and doesn't help anyone. If you have to, buy a cheap alarm clock and use that so you can keep your phone in another room to charge at night. Okay...stepping off the soapbox now. Besides, we still have two more lessons to cover.</p>
    <p>Social Connection was the hardest lesson of the entire module for me. Not because the suggestions were hard to implement, they aren't. The hardest part was realizing that while I was sitting behind the screen of my laptop and working my 60-hr/week job, I wasn't developing relationships. With my family, with friends, with anyone – unless you count my laptop as a relationship – which I don't. It was a sad revelation because I tend to be such a relationship oriented person. I'm starting to implement the suggestions from this lesson, and I was especially struck by a resource called <a href="#">Harborline</a>. It's just what I needed to get my relationships back where I want them, and to strengthen newly formed relationships.</p>
    <div class="figure figure-badge" role="img" aria-label="Round orange partner badge"></div>
    <p>The final lesson covers exercise and recovery. I think this one will be a real eye opener for some – especially those in the ancestral health community. But I think it's SO important because too many people don't realize the proper role of exercise in adrenal fatigue and HPA axis dysregulation recovery. There are some great suggestions for how you can exercise while recovering, and some solid reasons why overtraining is detrimental to your health as well.</p>
    <p>Whew – that was a lot in one module, huh? I didn't realize how much I'd learned until I started typing it all out here. My hope is that you something in this article strikes a chord with you and leaves wanting to learn more about this program. I cannot say enough good things about it. I wasn't sure I'd really feel better in just a few short weeks, and to be fair, they said from the outset that no one would be completely recovered in such little time, but the changes I've made are already making a difference.</p>
    <p>I can't wait to see what the Bonus Module holds for me next week. Until then, have a great weekend and take care of yourself and your body 🙂</p>
    <div class="links">
      <p>My thoughts on <a href="#">Module 1</a></p>
      <p>My thoughts on <a href="#">Module 2</a></p>
      <p>My thoughts on <a href="#">Module 3</a></p>
      <p>Check out Mara Holloway on <a href="#">Friendbook</a>, <a href="#">Chirpline</a>, <a href="#">Snapgrid</a>, and her <a href="#">website</a></p>
      <p>Check out Tessa Lindqvist on <a href="#">Friendbook</a>, <a href="#">Chirpline</a>, and her <a href="#">website</a></p>
    </div>
    <div class="read-more"><span class="btn">Read More</span></div>
  </article>

  <article class="post">
    <h1 class="post-title">April Essential Living Education Series</h1>
    <div class="post-meta">April 9, 2015 &nbsp; 🗨 Leave a comment</div>
    <p>During the month of April, I will be doing a series of Friendbook classes designed with you in mind. Topics range from skin care and personal care to Oils Through the Ages, Hormones, and how to have a Chemical Free Home.</p>
    <div class="figure figure-flyer" role="img" aria-label="Pink class schedule flyer"></div>
  </article>
</main>

<aside class="sidebar">
  <div class="widget">
    <div class="search">
      <div class="search-field">Search...</div>
      <div class="search-btn"><svg width="6" height="6" viewBox="0 0 10 10"><circle cx="4" cy="4" r="3" fill="none" stroke="#fff" stroke-width="1.5"/><line x1="6.2" y1="6.2" x2="9" y2="9" stroke="#fff" stroke-width="1.5"/></svg></div>
    </div>
  </div>
  <div class="widget">
    <h2 class="widget-title">Recent Posts</h2>
    <ul>
      <li><a href="#">Lifestyles of the Tired and Wired – Module 4 of Root Reset: Adrenal Fatigue</a></li>
      <li><a href="#">April Essential Living Education Series</a></li>
      <li><a href="#">Module 3: A Nice Supplement to the Program</a></li>
      <li><a href="#">What Do You Mean I Can't Have Coffee?! – Module 2 Root Reset: Adrenal Fatigue</a></li>
      <li><a href="#">DIY Emotional Regulation Blend</a></li>
    </ul>
  </div>
  <div class="widget">
    <h2 class="widget-title">Recent Comments</h2>
    <ul>
      <li><span class="mark"></span>Lifestyles of the Tired and Wired – Module 4 of Root Reset: Adrenal Fatigue | Birchwell Sprout Lady on <span class="by">What Do You Mean I Can't Have Coffee?! – Module 2</span></li>
      <li><span class="mark"></span>Lifestyles of the Tired and Wired – Module 4 of Root Reset: Adrenal Fatigue on <span class="by">Module 3: A Nice Supplement</span></li>
      <li><span class="mark"></span>Module 3: A Nice Supplement to the Program | Birchwell Sprout Lady on <span class="by">Module 1 group</span></li>
      <li><span class="mark"></span><span class="by">Nina</span> on Lifestyles of the Tired and Wired</li>
      <li><span class="mark"></span><span class="by">Owen Pratley</span> on Why I Chose Meadow Grove Essential Oils</li>
    </ul>
  </div>
  <div class="widget">
    <h2 class="widget-title">Archives</h2>
    <ul>
      <li><span class="mark"></span><a href="#">April 2015</a></li>
      <li><span class="mark"></span><a href="#">March 2015</a></li>
      <li><span class="mark"></span><a href="#">February 2015</a></li>
      <li><span class="mark"></span><a href="#">January 2015</a></li>
      <li><span class="mark"></span><a href="#">September 2014</a></li>
      <li><span class="mark"></span><a href="#">June 2014</a></li>
      <li><span class="mark"></span><a href="#">May 2014</a></li>
      <li><span class="mark"></span><a href="#">April 2014</a></li>
    </ul>
  </div>
  <div class="widget">
    <h2 class="widget-title">Categories</h2>
    <ul>
      <li><span class="mark"></span><a href="#">Three-Week Sugar Reset</a></li>
      <li><span class="mark"></span><a href="#">Adrenal Fatigue</a></li>
      <li><span class="mark"></span><a href="#">Articles</a></li>
      <li><span class="mark"></span><a href="#">DIY</a></li>
      <li><span class="mark"></span><a href="#">Essential Oils</a></li>
      <li><span class="mark"></span><a href="#">Real Food</a></li>
      <li><span class="mark"></span><a href="#">Uncategorized</a></li>
    </ul>
  </div>
</aside>

<div class="to-top"><svg width="6" height="6" viewBox="0 0 10 10"><polyline points="2,7 5,3 8,7" fill="none" stroke="#fff" stroke-width="1.6"/></svg></div>
</body>
</html>
```